Bright Oak Fitness Facility Business Cards

Business Card Design that incorporates the logo and tagline

Target Market(s)

Fitness, People Who Exercise

Contact Information for Business Card

2817 Mossgrove Bend Road
Tavares, Florida 32190
Phone: 352-555-Jump (5867)
www.brightoakfitness.example
info@brightoakfitness.example

Requirements
Must have
• Logo, Address, Website, email and tagline "More Than A Gym". Colors should be red/black/grey/white

```html
<!DOCTYPE html>
<html lang="en">
<head>
<meta charset="utf-8">
<title>Bright Oak Fitness – Business Card</title>
<link rel="stylesheet" href="https://fonts.googleapis.com/css2?family=Montserrat:wght@700&family=Open+Sans:wght@400&display=swap">
<style>
  :root {
    --page-bg: #e4e2df;
    --card-bg: #f7f5f2;
    --brand-red: #e0202e;
    --ink-black: #111111;
    --text-grey: #555555;
    --band-salmon: #ee8f78;
    --band-salmon-light: #f3a793;
  }
  html, body {
    margin: 0;
    width: 1200px;
    height: 1200px;
    overflow: hidden;
    background: var(--page-bg);
  }
  .canvas {
    width: 1200px;
    height: 1200px;
    display: flex;
    align-items: center;
    justify-content: center;
  }
  .business-card {
    position: relative;
    width: 1000px;
    height: 572px;
    background: var(--card-bg);
    overflow: hidden;
    box-shadow: 0 6px 24px rgba(0,0,0,0.15);
  }
  .tagline {
    position: absolute;
    top: 82px;
    left: 0;
    right: 0;
    margin: 0;
    text-align: center;
    font-family: "Montserrat", sans-serif;
    font-weight: 700;
    font-size: 62px;
    letter-spacing: 0.5px;
    color: var(--ink-black);
  }
  .tagline .accent { color: var(--brand-red); }
  .contact-list {
    position: absolute;
    top: 190px;
    left: 0;
    right: 0;
    margin: 0;
    padding: 0;
    list-style: none;
    text-align: center;
    font-family: "Open Sans", sans-serif;
    font-size: 24px;
    line-height: 40px;
    color: var(--text-grey);
  }
  .contact-list .label { color: var(--brand-red); }
  .brand-band {
    position: absolute;
    left: 0;
    bottom: 0;
    width: 1000px;
    height: 250px;
  }
  .wordmark {
    position: absolute;
    left: 0;
    right: 0;
    bottom: 60px;
    display: flex;
    align-items: center;
    justify-content: center;
    gap: 18px;
    font-family: "Montserrat", sans-serif;
    font-weight: 700;
    font-size: 54px;
    color: var(--ink-black);
    text-transform: uppercase;
  }
  .wordmark .mark-dot {
    width: 26px;
    height: 26px;
    border-radius: 50%;
    background: var(--brand-red);
  }
</style>
</head>
<body>
<main class="canvas">
  <article class="business-card">
    <h1 class="tagline"><span class="accent">MORE</span> THAN A <span class="accent">GYM</span></h1>
    <ul class="contact-list">
      <li><span class="label">T:</span> 352-555-Jump (5867)</li>
      <li><span class="label">A:</span> 2817 Mossgrove Bend Road, Tavares, Florida 32190</li>
      <li><span class="label">W:</span> www.brightoakfitness.example | <span class="label">E:</span> info@brightoakfitness.example</li>
    </ul>
    <svg class="brand-band" viewBox="0 0 1000 250" role="img" aria-label="Brand colour band">
      <defs>
        <linearGradient id="bandFill" x1="0" y1="0" x2="0" y2="1">
          <stop offset="0" stop-color="#f3a793"/>
          <stop offset="1" stop-color="#ee8f78"/>
        </linearGradient>
      </defs>
      <path d="M0 110 Q500 20 1000 110 L1000 250 L0 250 Z" fill="url(#bandFill)"/>
    </svg>
    <div class="wordmark"><span class="mark-dot"></span><span>Bright Oak Fitness</span></div>
  </article>
</main>
</body>
</html>
```